Math Help Website Needs New Design

Looking to refresh the design of my existing site (quillnumberdesk.com) to be easier on the eyes. I am fully capable of doing the HTML coding and have for years, but I don't have the eye for good design, colors, layout, and fonts. This is where I need help!

I need both a new design scheme and a new logo that matches. The overall functionality will be the same as the existing site, and should not be unrecognizable.

Target Market(s)

It should appeal to students (age 13-22) and their parents, so it should NOT be childish in appearance, nor should it be corporate.

Requirements
Must have
• Should be simple, easy-to-navigate, and neither childish nor corporate. I am looking for a design for both the homepage and a similar "content" page. Simple, bold colors are preferred. A logo should be prominent at the top, with a search bar nearby. Below that I need a similar navigational area like I already have. Then, I need about 200px wide ad space on the left of the main body area.

```html
<!DOCTYPE html>
<html lang="en">
<head>
<meta charset="utf-8">
<title>Quill Number Desk</title>
<link href="https://fonts.googleapis.com/css2?family=Baloo+2:wght@700;800&family=Comic+Neue:wght@400;700&family=Patrick+Hand+SC&family=Gochi+Hand&display=swap" rel="stylesheet">
<style>
:root{
  --sky-top:#8fd6f7;
  --sky-mid:#c9ecf6;
  --cream:#fbf3cf;
  --orange:#f7941d;
  --orange-dark:#e0700f;
  --nav-red:#e8380d;
  --red:#d21f0c;
  --green:#5a9b14;
  --green-btn:#7dbb16;
  --link:#1a6fd1;
  --arrow:#1a4fb5;
  --text:#333;
  --panel:#fff;
  --line:#d9d9d9;
  --footer:#efe4b4;
}
*{box-sizing:border-box;margin:0;padding:0}
html,body{width:1064px;height:1200px;overflow:hidden}
body{
  position:relative;
  font-family:"Comic Neue",sans-serif;
  color:var(--text);
  background:linear-gradient(180deg,var(--sky-top) 0,var(--sky-mid) 330px,#e8f3e2 560px,var(--cream) 800px,var(--cream) 100%);
}
.abs{position:absolute}
a{color:var(--link);text-decoration:none}

/* header */
.brand{left:163px;top:14px;display:flex;align-items:center;gap:12px}
.brand-mark{width:62px;height:62px;background:var(--orange);border-radius:8px}
.brand-name{font-family:"Baloo 2",sans-serif;font-weight:800;font-size:34px;line-height:1;color:var(--orange)}
.search{left:664px;top:32px;width:240px;height:31px;display:flex;border:2px solid var(--orange);border-radius:9px;overflow:hidden;background:linear-gradient(#fff,#e9e9e9)}
.search input{flex:1;border:0;background:transparent}
.search button{width:33px;border:0;background:var(--orange);display:flex;align-items:center;justify-content:center}

/* nav */
.nav{left:162px;top:97px;width:741px;height:35px;border-radius:6px;background:linear-gradient(#ffb23f,var(--orange));display:flex;list-style:none;overflow:hidden;box-shadow:0 1px 2px rgba(0,0,0,.2)}
.nav li{flex:1 1 auto;white-space:nowrap;font-family:"Patrick Hand SC",cursive;font-size:14px;color:#fff;display:flex;align-items:center;justify-content:center;border-right:1px solid #f9c472;padding:0 8px;font-style:italic}
.nav li:last-child{border:0}
.nav .active{background:var(--nav-red)}

/* banner */
.banner{left:162px;top:140px;width:741px;height:147px;background:#fff;border-radius:8px;padding:5px}
.banner-inner{position:relative;width:100%;height:100%;border-radius:5px;overflow:hidden;background:linear-gradient(90deg,#4ec3e2,#8adcf0 55%,#bfe9f5)}
.banner h1{position:absolute;left:17px;top:18px;font-family:"Gochi Hand",cursive;font-weight:400;font-size:58px;color:#fff;letter-spacing:2px;line-height:1}
.banner p{position:absolute;left:20px;top:86px;font-family:"Gochi Hand",cursive;font-size:30px;color:#fdf6a8;letter-spacing:2px}
.banner-photo{position:absolute;right:0;top:0;width:380px;height:100%;background:linear-gradient(90deg,rgba(140,200,230,0),#d9b79b 40%,#b07a5a)}

/* sidebar */
.sidebar{left:163px;top:299px;width:181px;height:491px;background:var(--panel);border-radius:7px;box-shadow:0 0 3px rgba(0,0,0,.1)}
.ad-tag{left:30px;top:15px;width:126px;height:32px;background:var(--orange);color:#fff;font-weight:700;font-size:17px;padding:5px 6px;border-radius:2px}
.ad-list{left:42px;top:54px;list-style:none;font-size:12px;line-height:19px}
.ad-list li::before{content:"▸";color:#999;margin-right:8px;font-size:10px}
.view-btn{left:95px;top:164px;width:56px;height:21px;background:var(--orange);color:#fff;border-radius:9px;font-weight:700;font-size:13px;text-align:center;line-height:21px}
.ad-card{left:30px;top:196px;width:126px;height:282px;border:1px solid #333;background:#fff}
.ad-photo{height:112px;background:linear-gradient(#fff,#e7d9c9 50%,#5aa7c9)}
.ad-band{height:28px;background:#d8181f;color:#fff;font-weight:700;font-size:14px;text-align:center;line-height:28px}
.ad-text{text-align:center;font-size:17px;line-height:24px;margin-top:10px;color:#222}
.ad-btn{display:block;margin:8px auto 0;width:50px;height:18px;background:#e01419;color:#fff;font-size:12px;text-align:center;line-height:18px}
.ad-foot{position:absolute;bottom:0;left:0;right:0;height:20px;background:#111;color:#f39c12;font-size:12px;text-align:center;line-height:20px}

/* main */
.main{left:358px;top:299px;width:543px;height:491px;background:var(--panel);border-radius:7px;box-shadow:0 0 3px rgba(0,0,0,.1)}
.head{font-family:"Patrick Hand SC",cursive;color:var(--red);font-size:24px;line-height:1;font-weight:400;white-space:nowrap}
.welcome{left:15px;top:17px}
.intro{left:15px;top:47px;width:515px;font-size:11.4px;line-height:14px}
.intro h3{color:var(--green);font-size:13.5px;font-weight:700}
.intro p+p{margin-top:12px}
.divider{left:15px;top:139px;width:513px;height:1px;background:var(--line)}
.vline{left:243px;top:155px;width:1px;height:315px;background:var(--line)}
.list{list-style:none;font-size:11.4px}
.list li{line-height:18.6px;display:flex;align-items:baseline;gap:6px;white-space:nowrap}
.list svg{flex:none;position:relative;top:1px}
.list.tight li{line-height:15.6px}
.posted{color:#333;padding-left:18px}
.col-a{left:15px;top:155px;width:215px}
.col-b{left:278px;top:155px;width:250px}
.sub-divider{height:1px;background:var(--line);margin:12px 0}

/* tools */
.tools{left:163px;top:811px;width:738px;height:304px;background:var(--panel);border-radius:7px}
.tabs{left:12px;top:11px;width:716px;height:28px;border-radius:6px;background:linear-gradient(var(--nav-red),#c72a09);display:flex;list-style:none;overflow:hidden}
.tabs li{flex:1 1 auto;justify-content:center;white-space:nowrap;font-family:"Patrick Hand SC",cursive;font-style:italic;color:#fff;font-size:14px;display:flex;align-items:center;padding:0 8px;border-right:1px solid #f26c4f}
.tabs li:last-child{border:0}
.tabs .active{background:var(--orange)}
.symbols{left:12px;top:48px;width:716px;display:flex;justify-content:space-between;padding:0 10px}
.sym{width:40px;text-align:center;font-family:"Times New Roman",serif;font-size:15px}
.sym .glyph{height:24px;display:flex;align-items:center;justify-content:center}
.label{font-size:13px;font-weight:700;color:var(--red);white-space:nowrap}
.help-box{display:inline-block;width:13px;height:13px;border:1px solid #446;font-size:9px;text-align:center;line-height:11px;color:#446;margin-left:4px}
.problem-label{left:12px;top:125px}
.problem{left:12px;top:150px;width:350px;height:88px;border:1px solid #bbb;border-radius:7px;background:linear-gradient(#fff,#ddd)}
.examples-label{left:380px;top:125px}
.examples{left:380px;top:150px;width:348px;height:88px;border:1px solid #bbb;border-radius:7px;background:#fff;padding:5px 6px;font-family:Arial,sans-serif;font-size:11px;line-height:15.5px;overflow:hidden}
.examples div{display:flex;align-items:center;gap:8px}
.examples i{width:10px;height:10px;border:1px solid #6b8fc5;font-style:normal;font-size:9px;line-height:8px;text-align:center;color:#355}
.format-a{left:12px;top:257px}
.show-btn{left:111px;top:253px;width:98px;height:25px;border-radius:9px;background:linear-gradient(#9bd33a,var(--green-btn));color:#fff;font-weight:700;font-size:13px;text-align:center;line-height:25px}
.format-b{left:240px;top:257px}
.select{left:339px;top:256px;width:261px;height:24px;border:1px solid #bbb;border-radius:7px;background:linear-gradient(#fff,#e4e4e4)}
.answer-btn{left:628px;top:253px;width:100px;height:25px;border-radius:9px;background:linear-gradient(#9bd33a,var(--green-btn));color:#fff;font-weight:700;font-size:13px;text-align:center;line-height:25px}

/* footer */
.footer{left:163px;top:1130px;width:738px;height:54px;background:var(--footer);border-radius:6px 6px 0 0}
.footer-links{left:10px;top:12px;font-size:9.6px;color:#333;display:flex;gap:6px;white-space:nowrap}
.footer-links .active{text-decoration:underline;color:#333}
.copy{left:10px;top:32px;font-size:9.6px;white-space:nowrap}
.social{right:10px;top:10px;display:flex;gap:14px}
.social span{width:34px;height:34px;border-radius:6px}
</style>
</head>
<body>

<header>
  <div class="abs brand">
    <span class="brand-mark"></span>
    <span class="brand-name">Quill Number Desk</span>
  </div>
  <form class="abs search">
    <input type="text" aria-label="Search">
    <button type="button" aria-label="Search">
      <svg width="16" height="16" viewBox="0 0 16 16"><circle cx="6.5" cy="6.5" r="4.5" fill="none" stroke="#fff" stroke-width="2.4"/><line x1="10" y1="10" x2="14.5" y2="14.5" stroke="#fff" stroke-width="2.6" stroke-linecap="round"/></svg>
    </button>
  </form>
</header>

<ul class="abs nav">
  <li class="active">HOME</li><li>ALGEBRA</li><li>GEOMETRY</li><li>TRIG</li><li>CALCULUS</li><li>STATISTICS</li><li>MORE SUBJECTS</li><li>MESSAGE BOARD</li>
</ul>

<section class="abs banner">
  <div class="banner-inner">
    <h1>KNOWLEGE</h1>
    <p>CAN NEVER BE EXCESS</p>
    <div class="banner-photo" role="img" aria-label="Photo of children learning together at a laptop"></div>
  </div>
</section>

<aside class="abs sidebar">
  <div class="abs ad-tag">Worksheets</div>
  <ul class="abs ad-list">
    <li><a>Maths</a></li><li><a>Physics</a></li><li><a>Chemistry</a></li><li><a>Biology</a></li><li><a>English</a></li><li><a>SST</a></li>
  </ul>
  <div class="abs view-btn">View</div>
  <div class="abs ad-card">
    <div class="ad-photo" role="img" aria-label="Photo of two smiling students with books"></div>
    <div class="ad-band">Classes 4<sup>th</sup> - 12<sup>th</sup></div>
    <div class="ad-text">Worksheets<br>&amp;<br>Exercises</div>
    <span class="ad-btn">View</span>
    <div class="ad-foot">studyleaf</div>
  </div>
</aside>

<main class="abs main">
  <h2 class="abs head welcome">WELCOME TO QUILL NUMBER DESK</h2>
  <div class="abs intro">
    <h3>Math Lessons -</h3>
    <p>Looking to understand a subject better, or maybe you don't understand what your textbook is trying to tell you? We have a collection of <a>algebra</a> and <a>geometry</a> lessons that you can view online right now.</p>
    <p>Ask your question on our <a>math help message board</a>. Just be sure to explain what you've tried to do and where you're stuck, and a friendly volunteer may try to assist you!</p>
  </div>
  <div class="abs divider"></div>
  <div class="abs vline"></div>

  <div class="abs col-a">
    <h2 class="head">WHAT'S NEW?</h2>
    <ul class="list" style="margin-top:12px">
      <li><svg width="12" height="10"><path d="M0 3h6V0l6 5-6 5V7H0z" fill="var(--arrow)"/></svg><a>Multiplying Polynomials</a></li>
      <li><svg width="12" height="10"><path d="M0 3h6V0l6 5-6 5V7H0z" fill="var(--arrow)"/></svg><a>Derivative of an Inverse Function</a></li>
      <li><svg width="12" height="10"><path d="M0 3h6V0l6 5-6 5V7H0z" fill="var(--arrow)"/></svg><a>Derivatives of Logs and Exps</a></li>
      <li><svg width="12" height="10"><path d="M0 3h6V0l6 5-6 5V7H0z" fill="var(--arrow)"/></svg><a>Differentiating Trig Functions</a></li>
    </ul>
    <div class="sub-divider"></div>
    <h2 class="head">MATH LESSON</h2>
    <ul class="list" style="margin-top:12px">
      <li><svg width="12" height="10"><path d="M0 3h6V0l6 5-6 5V7H0z" fill="var(--arrow)"/></svg><a>Algebra</a></li>
      <li><svg width="12" height="10"><path d="M0 3h6V0l6 5-6 5V7H0z" fill="var(--arrow)"/></svg><a>Geometry</a></li>
      <li><svg width="12" height="10"><path d="M0 3h6V0l6 5-6 5V7H0z" fill="var(--arrow)"/></svg><a>Trigonometry</a></li>
      <li><svg width="12" height="10"><path d="M0 3h6V0l6 5-6 5V7H0z" fill="var(--arrow)"/></svg><a>Calculus</a></li>
      <li><svg width="12" height="10"><path d="M0 3h6V0l6 5-6 5V7H0z" fill="var(--arrow)"/></svg><a>Statistics</a></li>
      <li><svg width="12" height="10"><path d="M0 3h6V0l6 5-6 5V7H0z" fill="var(--arrow)"/></svg><a>Sports Math</a></li>
      <li><svg width="12" height="10"><path d="M0 3h6V0l6 5-6 5V7H0z" fill="var(--arrow)"/></svg><a>Math Games</a></li>
      <li><svg width="12" height="10"><path d="M0 3h6V0l6 5-6 5V7H0z" fill="var(--arrow)"/></svg><a>Calculators</a></li>
    </ul>
  </div>

  <div class="abs col-b">
    <h2 class="head">CURRENT DISCUSSIONS</h2>
    <ul class="list tight" style="margin-top:12px">
      <li><svg width="12" height="10"><path d="M0 3h6V0l6 5-6 5V7H0z" fill="var(--arrow)"/></svg><a>2001 Harrow Press Geometry Teache...</a></li>
      <li class="posted">Posted by: kpro</li>
      <li><svg width="12" height="10"><path d="M0 3h6V0l6 5-6 5V7H0z" fill="var(--arrow)"/></svg><a>Polynomials and Synthetic Division Wo...</a></li>
      <li class="posted">Posted by: RonT</li>
      <li><svg width="12" height="10"><path d="M0 3h6V0l6 5-6 5V7H0z" fill="var(--arrow)"/></svg><a>Integrals involving inverse trig func...</a></li>
      <li class="posted">Posted by: seeagain</li>
      <li><svg width="12" height="10"><path d="M0 3h6V0l6 5-6 5V7H0z" fill="var(--arrow)"/></svg><a>Law of Sines/Cosines help.</a></li>
      <li class="posted">Posted by: tinybeel</li>
      <li><svg width="12" height="10"><path d="M0 3h6V0l6 5-6 5V7H0z" fill="var(--arrow)"/></svg><a>Help!! metric units</a></li>
      <li class="posted">Posted by: MattQS</li>
      <li><svg width="12" height="10"><path d="M0 3h6V0l6 5-6 5V7H0z" fill="var(--arrow)"/></svg><a>Law of Sines/Cosines help.</a></li>
      <li class="posted">Posted by: DrLane</li>
      <li><svg width="12" height="10"><path d="M0 3h6V0l6 5-6 5V7H0z" fill="var(--arrow)"/></svg><a>I hate word problems!</a></li>
      <li class="posted">Posted by: HillofOak</li>
      <li><svg width="12" height="10"><path d="M0 3h6V0l6 5-6 5V7H0z" fill="var(--arrow)"/></svg><a>Can someone help with this one? Maybe...</a></li>
      <li class="posted">Posted by: DrLane</li>
    </ul>
  </div>
</main>

<section class="abs tools">
  <ul class="abs tabs">
    <li class="active">BASIC MATH</li><li>PRE-ALGEBRA</li><li>ALGEBRA</li><li>TRIGONOMETRY</li><li>PRECALCULUS</li><li>CALCULUS</li><li>STATISTICS</li>
  </ul>
  <div class="abs symbols">
    <div class="sym"><div class="glyph"><svg width="20" height="12"><rect x="5" y="2" width="10" height="8" fill="#5b7fc4"/><path d="M3 1Q0 6 3 11M17 1Q20 6 17 11" stroke="#333" fill="none"/></svg></div>f(x)</div>
    <div class="sym"><div class="glyph"><svg width="20" height="12"><rect x="5" y="2" width="10" height="8" fill="#5b7fc4"/><path d="M3 1v10M17 1v10" stroke="#333"/></svg></div>ln</div>
    <div class="sym"><div class="glyph"><svg width="16" height="20"><rect x="3" y="1" width="10" height="7" fill="#5b7fc4"/><line x1="1" y1="10" x2="15" y2="10" stroke="#333"/><rect x="3" y="12" width="10" height="7" fill="#5b7fc4"/></svg></div>log<sub>□</sub></div>
    <div class="sym"><div class="glyph"><svg width="20" height="20"><g fill="#5b7fc4"><rect x="2" y="2" width="4" height="4"/><rect x="8" y="2" width="4" height="4"/><rect x="14" y="2" width="4" height="4"/><rect x="2" y="8" width="4" height="4"/><rect x="8" y="8" width="4" height="4"/><rect x="14" y="8" width="4" height="4"/><rect x="2" y="14" width="4" height="4"/><rect x="8" y="14" width="4" height="4"/><rect x="14" y="14" width="4" height="4"/></g><rect x=".5" y=".5" width="19" height="19" fill="none" stroke="#333"/></svg></div>∪</div>
    <div class="sym"><div class="glyph"><svg width="20" height="12"><rect x="5" y="2" width="10" height="8" fill="#5b7fc4"/><path d="M3 1v10M17 1v10" stroke="#333"/></svg></div>log</div>
    <div class="sym"><div class="glyph"><svg width="18" height="16"><rect x="1" y="4" width="11" height="11" fill="#5b7fc4"/><rect x="13" y="1" width="4" height="4" fill="#5b7fc4"/></svg></div>≥</div>
    <div class="sym"><div class="glyph"><svg width="18" height="16"><rect x="1" y="4" width="11" height="11" fill="#5b7fc4"/><rect x="13" y="1" width="4" height="4" fill="#5b7fc4"/></svg></div>≥</div>
    <div class="sym"><div class="glyph"><svg width="18" height="16"><rect x="1" y="1" width="11" height="11" fill="#5b7fc4"/><rect x="13" y="11" width="4" height="4" fill="#5b7fc4"/></svg></div>≤</div>
    <div class="sym"><div class="glyph"><svg width="22" height="16"><path d="M1 9l3-2 3 8 4-14h10" stroke="#333" fill="none"/><rect x="11" y="4" width="9" height="10" fill="#5b7fc4"/></svg></div>÷</div>
    <div class="sym"><div class="glyph"><svg width="22" height="16"><rect x="1" y="1" width="4" height="4" fill="#5b7fc4"/><path d="M1 9l3-2 3 8 4-14h10" stroke="#333" fill="none"/><rect x="11" y="4" width="9" height="10" fill="#5b7fc4"/></svg></div>π</div>
    <div class="sym"><div class="glyph"><svg width="24" height="12"><rect x="4" y="3" width="6" height="7" fill="#5b7fc4"/><rect x="14" y="3" width="6" height="7" fill="#5b7fc4"/><path d="M3 1Q0 6 3 11M21 1Q24 6 21 11" stroke="#333" fill="none"/></svg></div>∩</div>
  </div>

  <div class="abs label problem-label">Enter Problem : <span class="help-box">?</span></div>
  <div class="abs problem" aria-label="Problem input"></div>
  <div class="abs label examples-label">Examples :</div>
  <div class="abs examples">
    <div><i>+</i>Algebra Concepts and Expressions</div>
    <div><i>+</i>Points, Lines, and Line Segments</div>
    <div><i>+</i>Simplifying Polynomials</div>
    <div><i>+</i>Factoring Polynomials</div>
    <div><i>+</i>Linear Equations</div>
  </div>
  <div class="abs label format-a">Math Format :</div>
  <div class="abs show-btn">Show</div>
  <div class="abs label format-b">Math Format :</div>
  <div class="abs select"></div>
  <div class="abs answer-btn">Answer</div>
</section>

<footer class="abs footer">
  <nav class="abs footer-links">
    <a class="active">Home</a>|<span>Algebra</span>|<span>Geometry</span>|<span>Trig</span>|<span>Calculus</span>|<span>Statistics</span>|<span>More Subjects</span>|<span>Message Board</span>|<span>Owen Hartley</span>|<span>Sitemap</span>
  </nav>
  <div class="abs copy">Copyright © Quill Number Desk.All Right Reserved</div>
  <div class="abs social">
    <span style="background:#2f5ea8" aria-label="Social profile"></span>
    <span style="background:#3aaee0" aria-label="Social profile"></span>
  </div>
</footer>

</body>
</html>
```